New design for PeopleDesk

We are at the start of the process of evolving an existing business, and have just developed a new logo that will guide the look and feel of the rest of the site.

PeopleDesk.com.au will be the place to go for small business owners that need guidance and tools on how to look after HR functions such as recruitment and performance management amongst other aspects.

The existing site that is going to be evolved in www.hiringcornerfolk.com.au - while some of the content will remain, the entire look of the site needs to change, and a new homepage and other pages need to be developed.

For this project, we'd like the new homepage to be designed to lead the way for how the rest of the pages will look moving forward.

We're looking for a clean, clear and modern design. It should not feel cluttered or busy

The wireframe for the new homepage, and another landing page are attached.

Target Market(s)

Small and medium business owners - slightly male skew

Industry/Entity Type

Small Business

Requirements
Must have
• - Should be clean and simple
- The overall feel from the new logo (attached to the project) should be integrated into all elements of the site
- Should communicate that the site is easy to navigate
- Should communicate that the site is friendly and approachable
- Should communicate that the site is professional (for small businesses)
Nice to have
• This homepage for this site is quite a good design reference in terms of clean design.

http://www.choremoose.com/

For PeopleDesk though, the 3 boxes under the main image should appear above the fold though.

Also, happy for one other colour to be introduced to highlight call to action buttons etc.
Should not have
• Must not be cluttered
Should not introduce more than one additional colour to the existing colours from the logo

```html
<!DOCTYPE html>
<html lang="en">
<head>
<meta charset="utf-8">
<title>PeopleDesk – Homepage</title>
<link href="https://fonts.googleapis.com/css2?family=Arimo:wght@400;700&display=swap" rel="stylesheet">
<style>
:root{
  --blue-deep:#0b4c86;
  --blue-nav:#0e5ea6;
  --blue-nav-light:#1a77c4;
  --blue-head:#0d4a86;
  --blue-btn:#2a84e8;
  --blue-btn-dark:#1565c8;
  --text:#333;
  --muted:#555;
  --line:#c9c9c9;
  --footer:#4b4b4b;
  --footer-text:#f2f2f2;
  --page:#ffffff;
}
*{box-sizing:border-box;margin:0;padding:0}
html,body{width:1178px;height:1200px;overflow:hidden}
body{font-family:"Arimo",Arial,sans-serif;color:var(--text);background:var(--page);position:relative}
.top-rule{position:absolute;left:0;top:0;width:1178px;height:5px;background:var(--blue-deep)}
.header-band{position:absolute;left:0;top:5px;width:1178px;height:540px;background:linear-gradient(#dde9f2,#eef4f8 70%,#fff)}
.brand{position:absolute;left:10px;top:0;width:268px;height:96px;background:#fff;box-shadow:0 2px 6px rgba(0,0,0,.2);display:flex;align-items:center;justify-content:center;gap:12px}
.brand-dot{width:34px;height:34px;border-radius:50%;background:var(--blue-nav)}
.brand-name{font-size:34px;font-weight:700;color:var(--blue-nav)}
.contact{position:absolute;right:18px;top:16px;display:flex;align-items:center;gap:10px;font-size:16px;color:#222;line-height:20px}
.search{position:absolute;left:916px;top:67px;width:245px;height:36px;background:#fff;border:1px solid #ccc;display:flex;align-items:center}
.search span{flex:1;padding-left:12px;font-size:14px;color:#666}
.search i{width:36px;height:34px;border-left:1px solid #ccc;display:flex;align-items:center;justify-content:center;background:#f3f3f3}
.main-nav{position:absolute;left:10px;top:123px;width:1158px;height:50px;border-radius:6px;background:linear-gradient(var(--blue-nav-light),var(--blue-deep));display:flex;align-items:center;padding-left:14px;gap:4px}
.main-nav a{color:#fff;text-decoration:none;font-size:17px;font-weight:700;padding:8px 19px;border-radius:4px}
.main-nav a.active{background:linear-gradient(#3a9cf0,#1c78d4)}
.side-nav{position:absolute;left:10px;top:183px;width:269px;height:340px;background:var(--blue-deep)}
.side-nav a{display:flex;align-items:center;height:42.5px;padding-left:22px;color:#fff;text-decoration:none;font-size:17px;border-bottom:1px solid #0a3f70;background:linear-gradient(#1462a8,#0c4f8e)}
.side-nav a.active{background:linear-gradient(#5d5d5d,#383838)}
.side-nav a::before{content:"";width:7px;height:7px;border:2px solid #fff;border-radius:50%;margin-right:16px}
.hero{position:absolute;left:289px;top:183px;width:879px;height:340px;background:#e6eef6;box-shadow:0 0 6px rgba(0,0,0,.25)}
.hero-photo{position:absolute;left:0;top:0;width:398px;height:340px;background:linear-gradient(135deg,#dfe6ee,#c9b3a0 45%,#8a3b35 75%,#2f2f33)}
.hero-copy{position:absolute;left:428px;top:28px;width:400px}
.hero-copy h1{font-size:36px;line-height:38px;color:var(--blue-head);font-weight:700}
.hero-copy p{margin-top:14px;font-size:15px;line-height:21px;color:#444}
.btn{display:inline-flex;align-items:center;justify-content:center;color:#fff;text-decoration:none;border-radius:8px;background:linear-gradient(#4a9cf4,var(--btn-dark,#1565c8));box-shadow:0 1px 2px rgba(0,0,0,.3)}
.btn-learn{position:absolute;left:430px;top:249px;width:163px;height:42px;font-size:20px;font-weight:700}
.col{position:absolute;top:566px}
.col h2{font-size:24px;font-weight:700;color:var(--blue-head);margin-bottom:14px}
.about{left:13px;width:310px}
.about p{font-size:14px;line-height:19px;color:#333}
.ticks{list-style:none;margin-top:10px}
.ticks li{display:flex;align-items:center;gap:12px;height:42px;border-bottom:1px solid var(--line);font-size:14px;padding-left:8px}
.news{left:409px;width:340px}
.event{display:flex;gap:16px;padding:0 0 14px;margin-bottom:12px;border-bottom:1px solid var(--line)}
.date{width:36px;height:54px;flex:none;border-radius:4px;background:linear-gradient(#6d6d6d,#444);color:#fff;text-align:center;padding-top:8px}
.date b{display:block;font-size:20px}
.date small{font-size:9px}
.event h3{font-size:15px;color:var(--blue-head);margin-bottom:4px}
.event p{font-size:14px;line-height:18px;color:#333}
.social{left:825px;width:343px}
.person{border-bottom:1px solid var(--line);padding-bottom:12px;margin-bottom:14px}
.person-head{display:flex;gap:14px;align-items:center;margin-bottom:12px}
.avatar{width:49px;height:44px;background:linear-gradient(#a99a8c,#3c3f48)}
.person-head h3{font-size:15px;color:var(--blue-head)}
.person-head span{font-size:12px;color:#333}
.person p{font-size:14px;line-height:18px}
.btn-col{position:absolute;top:885px;height:36px;font-size:15px}
.footer{position:absolute;left:0;top:963px;width:1178px;height:237px;background:var(--footer);color:var(--footer-text)}
.footer h4{font-size:20px;font-weight:400;margin-bottom:12px}
.fcol{position:absolute;top:18px}
.fcol ul{list-style:none;font-size:14px;line-height:21px}
.fcol p{font-size:14px;line-height:21px;width:420px}
.signup{display:flex;gap:12px;margin-top:14px}
.signup span{width:276px;height:34px;background:#6e6e6e;border:1px solid #8a8a8a}
.signup a{width:106px;height:36px;font-size:16px;font-weight:700}
.circles{display:flex;gap:10px}
.circles i{width:34px;height:34px;border-radius:50%;background:linear-gradient(#e8e8e8,#9a9a9a)}
.foot-brand{margin-top:34px;display:flex;align-items:center;gap:10px;color:#777;font-size:30px;font-weight:700}
.foot-brand i{width:32px;height:32px;border-radius:50%;background:#6a6a6a}
</style>
</head>
<body>
<div class="top-rule"></div>
<div class="header-band"></div>

<header>
  <div class="brand"><span class="brand-dot"></span><span class="brand-name">PeopleDesk</span></div>
  <div class="contact">
    <svg width="34" height="28" viewBox="0 0 34 28"><path d="M3 9c0-5 28-5 28 0v3h-7V9H10v3H3z" fill="#333"/><rect x="8" y="13" width="18" height="13" rx="3" fill="#333"/><circle cx="17" cy="19" r="3.5" fill="#ddd"/></svg>
    <div>+ (00) 55 01 48302716<br>+ (00) 55 01 48302715</div>
  </div>
  <div class="search"><span>Search...</span><i><svg width="18" height="18" viewBox="0 0 18 18"><circle cx="7" cy="7" r="5" fill="none" stroke="#555" stroke-width="2"/><path d="M11 11l5 5" stroke="#555" stroke-width="2.5"/></svg></i></div>
</header>

<nav class="main-nav">
  <a class="active" href="#">Attract</a><a href="#">Recruit</a><a href="#">Induction</a><a href="#">Engage</a><a href="#">Performance</a><a href="#">Termination &amp; Community</a><a href="#">Management</a><a href="#">Redundancy</a>
</nav>

<nav class="side-nav">
  <a class="active" href="#">Attract</a><a href="#">Recruit</a><a href="#">Induction</a><a href="#">Engage</a><a href="#">Performance</a><a href="#">Termination &amp;Community</a><a href="#">Management</a><a href="#">Redundancy aa</a>
</nav>

<section class="hero">
  <div class="hero-photo" role="img" aria-label="Photo of a smiling team of three professionals"></div>
  <div class="hero-copy">
    <h1>Lorem Ipsum is simply Dummy</h1>
    <p>Lorem Ipsum is simply dummy text of the printing and typesetting industry. Lorem Ipsum has been the industry's standard dummy text ever since the 1500s, when an unknown printer took a galley of type and scrambled.</p>
  </div>
  <a class="btn btn-learn" href="#">Learn more</a>
</section>

<section class="col about">
  <h2>About</h2>
  <p>We pride ourselves on our approach and understanding, our team is made up of both high levels of knowledge and a proven track record in starting, funding and advising businesses.</p>
  <ul class="ticks">
    <li><svg width="16" height="14" viewBox="0 0 16 14"><path d="M1 7l5 5L15 2" fill="none" stroke="#555" stroke-width="3"/></svg>Equity Funding</li>
    <li><svg width="16" height="14" viewBox="0 0 16 14"><path d="M1 7l5 5L15 2" fill="none" stroke="#555" stroke-width="3"/></svg>Strategic Advisory</li>
    <li><svg width="16" height="14" viewBox="0 0 16 14"><path d="M1 7l5 5L15 2" fill="none" stroke="#555" stroke-width="3"/></svg>Capital Raising Strategies</li>
    <li><svg width="16" height="14" viewBox="0 0 16 14"><path d="M1 7l5 5L15 2" fill="none" stroke="#555" stroke-width="3"/></svg>Management &amp; Administration</li>
  </ul>
</section>

<section class="col news">
  <h2>News/community</h2>
  <div class="event"><div class="date"><b>22</b><small>SEP</small></div><div><h3>No Allocables</h3><p>Lorem ipsum dolor sit amet, consectetur no urna adipiscing elit. Nullam sit amet.</p></div></div>
  <div class="event"><div class="date"><b>24</b><small>SEP</small></div><div><h3>No Allocables</h3><p>Lorem ipsum dolor sit amet, consectetur no adipiscing elit. Nullam sit amet urna.</p></div></div>
  <div class="event" style="border:0"><div class="date"><b>25</b><small>SEP</small></div><div><h3>No Allocables</h3><p>Lorem ipsum dolor sit amet, no urna adipiscing elit. Nullam sit amet.</p></div></div>
</section>

<section class="col social">
  <h2>Social links/Partners</h2>
  <div class="person">
    <div class="person-head"><div class="avatar" role="img" aria-label="Portrait of Darren Coble"></div><div><h3>Darren Coble</h3><span>CEO &amp; Co-Founder - Brightlane.com</span></div></div>
    <p>Kristie is a founding member of Tallow Partners. Prior to this, she was a Partner at The Greyholt</p>
  </div>
  <div class="person" style="border:0">
    <div class="person-head"><div class="avatar" role="img" aria-label="Portrait of Miles Harte"></div><div><h3>Miles Harte</h3><span>Founder - Quillfield.com</span></div></div>
    <p>Proin viverra nunc a neque convallis ultricies eget euismod risus. Vivamus feugiat viverra tellus</p>
  </div>
</section>

<a class="btn btn-col" href="#" style="left:17px;width:120px">Read More</a>
<a class="btn btn-col" href="#" style="left:412px;width:165px">All Events / News</a>
<a class="btn btn-col" href="#" style="left:832px;width:165px">Read All Reviews</a>

<footer class="footer">
  <div class="fcol" style="left:34px"><h4>Quick links</h4><ul><li>Home</li><li>About</li><li>Work</li><li>Blog</li><li>Contact</li><li>Client Login</li></ul></div>
  <div class="fcol" style="left:237px"><h4>Powered By</h4><ul><li>PageForge</li><li>(hs) Harbor Stack</li><li>Live Stats</li><li>OrbitDesk</li><li>PostFinch</li><li>LedgerLeaf</li></ul></div>
  <div class="fcol" style="left:449px"><h4>Receive Email Updates</h4><p>Lorem Ipsum is simply dummy text of the printing and typesetting industry. Lorem Ipsum has been the industry's standard dummy text when an unknown printer.</p>
    <div class="signup"><span></span><a class="btn" href="#">SIGN UP</a></div></div>
  <div class="fcol" style="left:934px;top:22px"><h4>Social Network</h4><div class="circles"><i></i><i></i><i></i></div>
    <div class="foot-brand"><i></i>PeopleDesk</div></div>
</footer>
</body>
</html>
```